SEAFOOD PACKAGING (Products for consumer)

We are looking to create packaging for various seafood products such as octopus and squid. We plan to sell our products in upscale supermarkets.

We are specializing in cut octopus this time.

Please include our company logo. Also, please leave a transparent area so that customers can see the product inside.
Updates

We want to show what is inside, so a picture of the octopus is not required. We need something simple and sophisticated.

Target Market(s)

upscale store in US and ASIA

Industry/Entity Type

Fisheries dealer

Requirements
Must have
• Please include the attached logo,Blue one is preferred.Please leave a transparent part so that the contents of the product can be seen by the consumer.1. product name on packaging →CUT OCTOPUS,TAKO SASHIMI,Highest quality,Top quality etc... 3. What text information should be on the packaging →(It may be edited, but this is the image) The raw materials are caught in a very clean environment and processed in a modern factory with KVT certification. We are committed to additive-free products. 4. Packing size(cm/inch)→it will be about 19cm*22cm. 5. what kind of packaging do you use →PP or PA 6. dll →ai,jag
Nice to have
• https://plenvik.com/shots/4829173-Merulo-Prawn We need something simple and sophisticated like this one.
Should not have
• We want to show what is inside, so a picture of the octopus is not required. We need something simple and sophisticated.

```html
<!DOCTYPE html>
<html lang="en">
<head>
<meta charset="utf-8">
<title>Cut Octopus – Tako Sashimi Pack</title>
<link rel="stylesheet" href="https://fonts.googleapis.com/css2?family=Oswald:wght@500;600;700&family=Roboto+Condensed:wght@400;500;700&display=swap">
<style>
  :root {
    --stage: #939598;
    --film: #d6d7d9;
    --label-white: #fbf9f8;
    --brand-blue: #1170b9;
    --logo-blue: #1f5fa8;
    --ink: #2b2b2b;
    --rule: #6b6b6b;
  }
  * { box-sizing: border-box; margin: 0; padding: 0; }
  html, body { width: 1200px; height: 900px; overflow: hidden; }
  body { background: var(--stage); position: relative; font-family: "Roboto Condensed", sans-serif; }

  .pack-film {
    position: absolute; left: 228px; top: 20px;
    width: 745px; height: 860px;
    background: var(--film);
  }

  .front-label {
    position: absolute; left: 211px; top: 0;
    width: 318px; height: 380px;
  }
  .front-label svg { position: absolute; inset: 0; }
  .claim-badges {
    position: absolute; top: 44px; left: 0; right: 0;
    display: flex; justify-content: center; gap: 16px;
  }
  .claim-badge {
    width: 44px; height: 44px; border-radius: 50%;
    border: 2px solid var(--logo-blue);
  }
  .product-title {
    position: absolute; top: 138px; left: 0; right: 0;
    text-align: center; color: #fff;
    font-family: "Oswald", sans-serif; font-weight: 600;
  }
  .product-title .main {
    display: block; font-size: 62px; line-height: 58px; letter-spacing: 1px;
  }
  .product-title .sub {
    display: inline-block; margin-top: 8px; padding-top: 4px;
    border-top: 2px solid #fff;
    font-size: 36px; line-height: 40px; letter-spacing: 1.5px; width: 232px;
  }
  .product-attributes {
    position: absolute; bottom: 10px; left: 0; right: 0; text-align: center;
    font-family: "Oswald", sans-serif; font-weight: 500; font-size: 17px;
    letter-spacing: 1px; color: var(--ink);
  }

  .brand-mark {
    position: absolute; left: 128px; top: 440px;
    display: flex; align-items: center; gap: 40px;
  }
  .brand-dot { width: 120px; height: 120px; border-radius: 50%; background: var(--logo-blue); }
  .brand-name {
    font-family: "Oswald", sans-serif; font-weight: 700; font-size: 112px;
    line-height: 1; letter-spacing: 14px; color: var(--logo-blue);
  }

  .back-label {
    position: absolute; left: 211px; top: 614px;
    width: 318px; height: 246px;
    color: var(--ink); text-align: center; text-transform: uppercase;
  }
  .back-label svg { position: absolute; inset: 0; }
  .back-copy { position: relative; padding: 24px 20px 0; }
  .origin-statement { font-size: 11.5px; line-height: 14px; letter-spacing: .3px; }
  .commitment {
    margin-top: 10px; padding: 6px 0;
    border-top: 1px solid var(--rule); border-bottom: 1px solid var(--rule);
    font-size: 11.5px; letter-spacing: .3px;
  }
  .pack-facts {
    margin-top: 14px; display: flex; align-items: center; justify-content: space-between;
  }
  .fact { width: 108px; border-top: 1px solid var(--rule); border-bottom: 1px solid var(--rule); padding: 3px 0; }
  .fact .big { font-size: 14px; font-weight: 500; line-height: 15px; }
  .fact .small { font-size: 11px; line-height: 13px; }
  .seal { width: 58px; height: 58px; border-radius: 50%; background: var(--brand-blue); }
</style>
</head>
<body>
  <section class="pack-film" aria-label="Transparent film area showing the cut octopus inside">
    <div class="front-label">
      <svg width="318" height="380" viewBox="0 0 318 380" aria-hidden="true">
        <path d="M0 0 H318 V368 Q318 380 306 380 H12 Q0 380 0 368 Z" fill="var(--label-white)"/>
        <path d="M0 118 Q150 82 318 108 V335 H0 Z" fill="var(--brand-blue)"/>
      </svg>
      <div class="claim-badges">
        <span class="claim-badge"></span>
        <span class="claim-badge"></span>
        <span class="claim-badge"></span>
      </div>
      <h1 class="product-title">
        <span class="main">CUT</span>
        <span class="main">OCTOPUS</span>
        <span class="sub">TAKO SASHIMI</span>
      </h1>
      <p class="product-attributes">RAW &bull; FRESH &bull; CLEAN</p>
    </div>

    <div class="brand-mark">
      <span class="brand-dot"></span>
      <span class="brand-name">MARLEN</span>
    </div>

    <div class="back-label">
      <svg width="318" height="246" viewBox="0 0 318 246" aria-hidden="true">
        <path d="M0 6 L6 0 L12 6 L18 0 L24 6 L30 0 L36 6 L42 0 L48 6 L54 0 L60 6 L66 0 L72 6 L78 0 L84 6 L90 0 L96 6 L102 0 L108 6 L114 0 L120 6 L126 0 L132 6 L138 0 L144 6 L150 0 L156 6 L162 0 L168 6 L174 0 L180 6 L186 0 L192 6 L198 0 L204 6 L210 0 L216 6 L222 0 L228 6 L234 0 L240 6 L246 0 L252 6 L258 0 L264 6 L270 0 L276 6 L282 0 L288 6 L294 0 L300 6 L306 0 L312 6 L318 0 V246 H0 Z" fill="var(--label-white)"/>
      </svg>
      <div class="back-copy">
        <p class="origin-statement">The raw materials are caught in a very clean<br>environment and processed in a modern factory<br>with KVT certification</p>
        <p class="commitment">We are committed to additive-free products</p>
        <div class="pack-facts">
          <div class="fact">
            <p class="big">Net Wt.</p>
            <p class="small">16OZ (1LB) 454g</p>
          </div>
          <span class="seal"></span>
          <div class="fact">
            <p class="big">100%</p>
            <p class="small">Natural Product</p>
          </div>
        </div>
      </div>
    </div>
  </section>
</body>
</html>
```